Portfolio site - Need a basic WordPress or SquareSpace site

I need a portfolio site where I have the option to keep updating it on my own. Therefore, I'm guessing I need one that uses WordPress or SquareSpace. I just need a simple and elegant design. I'm a writer (scholarly, fiction and journalism).

Target Market(s)

Adult

Industry/Entity Type

Writer

Number of Pages Required

4 page

Font styles to use
Serif

Colors
b7a5cd
e667a6
85abd2

Requirements
Must have
• Easily updatable features. I'll have to publish links and small blurbs from time to time. And maybe the occasional image.
• Pages should be:
• Home
• Work
• Press
• Contact

```html
<!DOCTYPE html>
<html lang="en">
<head>
<meta charset="utf-8">
<title>Maren Aldous — Writer</title>
<link href="https://fonts.googleapis.com/css2?family=Montserrat:wght@300;400;500;600;700&display=swap" rel="stylesheet">
<style>
  :root {
    --pink: #e667a6;
    --blue: #85abd2;
    --lilac: #b7a5cd;
    --grey: #d7d7d7;
    --white: #ffffff;
    --ink: #2b2b2b;
    --muted: #6a6a6a;
    --font: "Montserrat", "Helvetica Neue", Arial, sans-serif;
  }
  * { box-sizing: border-box; margin: 0; padding: 0; }
  html, body { width: 1200px; height: 3629px; overflow: hidden; }
  body { font-family: var(--font); color: var(--ink); background: var(--white); position: relative; }

  /* Hero */
  .hero {
    position: absolute; left: 0; top: 0; width: 1200px; height: 480px;
    background: linear-gradient(135deg, #c7cfdb 0%, #b4bfce 45%, #9eabbe 100%);
    color: var(--white); text-align: center;
  }
  .hero::after { content: ""; position: absolute; inset: 0; background: rgba(120,140,175,0.25); }
  .hero > * { position: relative; z-index: 1; }
  .brand { position: absolute; left: 246px; top: 28px; font-size: 19px; font-weight: 600; color: var(--ink); letter-spacing: .5px; z-index: 2; }
  .nav { position: absolute; right: 244px; top: 34px; display: flex; gap: 22px; z-index: 2; }
  .nav a { color: var(--white); text-decoration: none; font-size: 12px; }
  .hero h1 { position: absolute; left: 300px; width: 600px; top: 170px; font-size: 30px; font-weight: 700; line-height: 1.25; }
  .hero p { position: absolute; left: 300px; width: 600px; top: 294px; font-size: 12px; font-weight: 300; }
  .btn-outline {
    position: absolute; left: 552px; top: 334px; width: 96px; height: 30px; border: 1px solid var(--white);
    font-size: 9px; font-weight: 600; line-height: 28px; letter-spacing: 1px; color: var(--white);
  }

  /* Intro row */
  .photo { position: absolute; }
  .intro-left { left: 0; top: 484px; width: 398px; height: 484px; background: linear-gradient(150deg, #bdbdbd, #6f6f6f); }
  .intro-right { left: 804px; top: 484px; width: 396px; height: 484px; background: linear-gradient(160deg, #8a8a8a, #cfcfcf 60%, #9c9c9c); }
  .intro-card {
    position: absolute; left: 402px; top: 458px; width: 398px; height: 538px; background: var(--pink);
    color: var(--white); text-align: center; padding: 170px 58px 0; z-index: 3;
  }
  .eyebrow { font-size: 10px; font-weight: 400; }
  .intro-card h2 { font-size: 28px; font-weight: 700; margin: 10px 0 22px; }
  .intro-card p { font-size: 14px; line-height: 1.55; font-weight: 300; }

  /* Work */
  .work {
    position: absolute; left: 0; top: 972px; width: 1200px; height: 480px; background: var(--blue);
    color: var(--white); text-align: center; padding-top: 96px; overflow: hidden;
  }
  .work h2 { font-size: 28px; font-weight: 700; margin: 8px 0 26px; }
  .work p { width: 790px; margin: 0 auto 20px; font-size: 13.5px; line-height: 1.6; font-weight: 300; }
  .work .faint-name { position: absolute; left: 0; right: 0; bottom: -14px; font-size: 46px; font-weight: 600; color: rgba(255,255,255,0.18); margin: 0; width: auto; }

  /* Gallery */
  .gallery { position: absolute; left: 0; top: 1457px; width: 1200px; display: grid; grid-template-columns: 398px 398px 398px; grid-template-rows: 350px 350px; gap: 3px; }
  .gallery div:nth-child(1) { background: linear-gradient(90deg, #2f5a3d, #2d3f86 35%, #a7422e 60%, #1d1d1d); }
  .gallery div:nth-child(2) { background: linear-gradient(135deg, #3b2a22 0%, #8c6c55 30%, #f1ede8 60%); }
  .gallery div:nth-child(3) { background: linear-gradient(135deg, #f4ecdc, #d8c8a8 50%, #40424e); }
  .gallery div:nth-child(4) { background: linear-gradient(160deg, #5a5a5a, #b9b9b9 50%, #6b6b6b); }
  .gallery div:nth-child(5) { background: linear-gradient(160deg, #2e2a27, #9c8c78 40%, #efe9df 70%); }
  .gallery div:nth-child(6) { background: linear-gradient(180deg, #1d1d1d, #6d6d6d 50%, #1f1f1f); }

  /* Press */
  .press { position: absolute; left: 0; top: 2166px; width: 1200px; height: 786px; background: var(--lilac); color: var(--white); text-align: center; }
  .press h2 { position: absolute; left: 0; right: 0; top: 98px; font-size: 26px; font-weight: 700; }
  .press .lede { position: absolute; left: 0; right: 0; top: 152px; font-size: 14px; font-weight: 300; }
  .press-grid { position: absolute; left: 249px; top: 198px; width: 704px; display: grid; grid-template-columns: repeat(3, 228px); column-gap: 10px; row-gap: 24px; text-align: left; }
  .quote { position: relative; }
  .quote-body { background: var(--white); color: var(--ink); height: 196px; padding: 22px 18px; font-size: 10px; line-height: 1.75; position: relative; }
  .quote-body::after { content: ""; position: absolute; left: 18px; bottom: -8px; border-left: 8px solid transparent; border-right: 8px solid transparent; border-top: 8px solid var(--white); }
  .quote.featured .quote-body { background: var(--pink); color: var(--white); }
  .quote.featured .quote-body::after { border-top-color: var(--pink); }
  .byline { display: flex; align-items: center; gap: 6px; margin-top: 8px; padding-left: 8px; }
  .byline .dot { width: 22px; height: 22px; border-radius: 50%; background: var(--white); flex: none; }
  .byline strong { display: block; font-size: 8px; font-weight: 600; }
  .byline span { display: block; font-size: 6.5px; font-weight: 300; }

  /* Contact */
  .contact { position: absolute; left: 0; top: 2957px; width: 1200px; height: 535px; background: var(--grey); text-align: center; }
  .contact .eyebrow { position: absolute; left: 0; right: 0; top: 52px; }
  .contact .intro { position: absolute; left: 0; right: 0; top: 98px; font-size: 15px; line-height: 1.5; }
  .form { position: absolute; left: 363px; top: 172px; width: 474px; text-align: left; font-size: 10px; }
  .form label { display: block; margin-bottom: 4px; }
  .field { background: var(--white); height: 24px; }
  .name-row { display: flex; gap: 10px; }
  .name-row > div { flex: 1; }
  .hint { font-size: 7px; margin-top: 4px; color: var(--muted); }
  .group { margin-bottom: 16px; }
  .field.tall { height: 60px; }
  .submit { display: block; width: 98px; height: 30px; margin: 24px auto 0; border: 1.5px solid var(--ink); background: transparent; font: 600 9px var(--font); letter-spacing: 1px; }

  /* Footer */
  .footer { position: absolute; left: 0; top: 3492px; width: 1200px; height: 137px; background: var(--white); }
  .footer .brand { left: 249px; top: 54px; }
  .footer small { position: absolute; right: 250px; top: 56px; font-size: 9px; text-align: right; line-height: 1.6; }
</style>
</head>
<body>

<header class="hero" role="img" aria-label="Desk with an open notebook and a jar of coloured markers">
  <div class="brand">Maren Aldous</div>
  <nav class="nav"><a href="#">Home</a><a href="#">Work</a><a href="#">Press</a><a href="#">Contact</a></nav>
  <h1>Lorem Ipsum is simply dummy text of the printing and typesetting industry.</h1>
  <p>Lorem ipsum is simply dummy text of the printing and typesetting</p>
  <div class="btn-outline">LEARN MORE</div>
</header>

<div class="photo intro-left" role="img" aria-label="Open book with a dried leaf on its pages"></div>
<section class="intro-card">
  <div class="eyebrow">Welcome to</div>
  <h2>Maren Aldous</h2>
  <p>Lorem ipsum has been the industry's standard dummy text ever since the 1500s, when an unknown printer took a galley of type and scrambled it to make a type specimen book.</p>
</section>
<div class="photo intro-right" role="img" aria-label="Writer typing on a laptop, seen from above"></div>

<section class="work">
  <div class="eyebrow">Work</div>
  <h2>Lorem Ipsum</h2>
  <p>Lorem Ipsum is simply dummy text of the printing and typesetting industry. Lorem Ipsum has been the industry's standard dummy text ever since the 1500s, when an unknown printer took a galley of type and scrambled it to make a type specimen book.</p>
  <p>Lorem Ipsum has been the industry's standard dummy text ever since the 1500s, when an unknown printer took a galley of type and scrambled it to make a type specimen book.</p>
  <p class="faint-name">Maren Aldous</p>
</section>

<section class="gallery">
  <div role="img" aria-label="Row of hardback book spines on a shelf"></div>
  <div role="img" aria-label="Hand writing with a pen in a notebook"></div>
  <div role="img" aria-label="Man reading a newspaper"></div>
  <div role="img" aria-label="Stack of folded newspapers"></div>
  <div role="img" aria-label="Open blank notebook on a table"></div>
  <div role="img" aria-label="Keys of a vintage typewriter"></div>
</section>

<section class="press">
  <h2>Press</h2>
  <p class="lede">Lorem Ipsum is simply dummy text of the printing and typesetting industry.</p>
  <div class="press-grid">
    <article class="quote featured"><div class="quote-body">Lorem ipsum is simply dummy text of the printing and typesetting industry. Lorem ipsum has been the industry's standard dummy text ever since the 1500s, when an unknown printer took a galley of type and scrambled it to make a type specimen book.</div><div class="byline"><i class="dot"></i><div><strong>Lorem ipsum is simply</strong><span>dummy text of printing</span></div></div></article>
    <article class="quote"><div class="quote-body">Lorem ipsum is simply dummy text of the printing and typesetting industry. Lorem ipsum has been the industry's standard dummy text ever since the 1500s, when an unknown printer took a galley of type and scrambled it to make a type specimen book.</div><div class="byline"><i class="dot"></i><div><strong>Lorem ipsum is simply</strong><span>dummy text of printing</span></div></div></article>
    <article class="quote"><div class="quote-body">Lorem ipsum is simply dummy text of the printing and typesetting industry. Lorem ipsum has been the industry's standard dummy text ever since the 1500s, when an unknown printer took a galley of type and scrambled it to make a type specimen book.</div><div class="byline"><i class="dot"></i><div><strong>Lorem ipsum is simply</strong><span>dummy text of printing</span></div></div></article>
    <article class="quote"><div class="quote-body">Lorem ipsum is simply dummy text of the printing and typesetting industry. Lorem ipsum has been the industry's standard dummy text ever since the 1500s, when an unknown printer took a galley of type and scrambled it to make a type specimen book.</div><div class="byline"><i class="dot"></i><div><strong>Lorem ipsum is simply</strong><span>dummy text of printing</span></div></div></article>
    <article class="quote"><div class="quote-body">Lorem ipsum is simply dummy text of the printing and typesetting industry. Lorem ipsum has been the industry's standard dummy text ever since the 1500s, when an unknown printer took a galley of type and scrambled it to make a type specimen book.</div><div class="byline"><i class="dot"></i><div><strong>Lorem ipsum is simply</strong><span>dummy text of printing</span></div></div></article>
    <article class="quote"><div class="quote-body">Lorem ipsum is simply dummy text of the printing and typesetting industry. Lorem ipsum has been the industry's standard dummy text ever since the 1500s, when an unknown printer took a galley of type and scrambled it to make a type specimen book.</div><div class="byline"><i class="dot"></i><div><strong>Lorem ipsum is simply</strong><span>dummy text of printing</span></div></div></article>
  </div>
</section>

<section class="contact">
  <div class="eyebrow">Contact Us</div>
  <p class="intro">It's an honor to connect with you. Please reach out below!<br>For direct emails, please contact us at info@marenaldous.com</p>
  <div class="form">
    <div class="group">
      <label>Name *</label>
      <div class="name-row">
        <div><div class="field"></div><div class="hint">First Name</div></div>
        <div><div class="field"></div><div class="hint">Last Name</div></div>
      </div>
    </div>
    <div class="group"><label>Email Address *</label><div class="field"></div></div>
    <div class="group"><label>Subject *</label><div class="field"></div></div>
    <div class="group"><label>Message *</label><div class="field tall"></div></div>
    <button class="submit" type="button">SUBMIT</button>
  </div>
</section>

<footer class="footer">
  <div class="brand">Maren Aldous</div>
  <small>Copyright © 2018 Maren Aldous. All Rights Reserved.</small>
</footer>

</body>
</html>
```